Corporate flyer highlighting service offering for PR agency

A corporate flyer is needed for a new service offering that we are doing. The product name is HarborLeap it is a marketing and communications services offering for companies who are getting ready to sell their business. If we are really happy with the designer's work, there will be a great deal more projects. I am looking for a clean design with a few pops of color from my site. https://quillmarsh.partners. I am looking for a good design with data in sections. I am looking for a clean design that feels high-end but not cluttered. Please do not use images of people. Please see the following examples of types of designs I like.
https://www.tackboard.example/pin/839201746530918264/
https://www.tackboard.example/pin/402918375561029847/
https://assets.stockvale.example/corporate-flyer-template-KRTPMB
https://designbrook.example/item/corporate-flyer-template/81046395?s_rank=8
https://assets.stockvale.example/corporate-business-flyer-template-93PX7D

I had to place the project on hold as I choose the wrong type of project and did not get many designs as a result. I am reposting this with an updated brief.

Target Market(s)

Business sellers and brokers

Industry/Entity Type

Marketing for business sellers

Font styles to use
Sans Serif

Requirements
Must have
• Good quality design with content in sections. Clean and high end feeling is a must.
Should not have
• A lot of images of people.

```html
<!DOCTYPE html>
<html lang="en">
<head>
<meta charset="utf-8">
<title>HarborLeap Flyer</title>
<link href="https://fonts.googleapis.com/css2?family=Montserrat:ital,wght@0,400;0,500;0,600;0,700;1,500;1,600&display=swap" rel="stylesheet">
<style>
:root{
  --bg:#d9dbde;
  --navy:#1c3552;
  --blue:#2f86cf;
  --sky:#38a9e4;
  --orange:#f15a24;
  --amber:#f3a31b;
  --green:#69a844;
  --lime:#9fd04a;
  --ink:#2a2f36;
  --white:#ffffff;
}
*{box-sizing:border-box;margin:0;padding:0}
html,body{width:1200px;height:775px;overflow:hidden}
body{background:var(--bg);font-family:'Montserrat',sans-serif;color:var(--ink);display:flex;gap:40px;padding:12px 50px}
.page{width:530px;height:750px;background:var(--white);display:flex;flex-direction:column;overflow:hidden;box-shadow:0 2px 10px rgba(0,0,0,.18);font-size:6.1px;line-height:1.32}
.tick{width:6px;height:6px;flex:none;margin-top:1px}
.list{list-style:none;display:flex;flex-direction:column;gap:2.5px}
.list li{display:flex;gap:4px}
.list.tight{gap:1.5px}
b{font-weight:700}
/* hero */
.hero{height:225px;flex:none;background:var(--navy);position:relative;color:var(--white);padding:22px 26px 0}
.hero-photo{position:absolute;right:0;top:0;width:290px;height:190px;background:linear-gradient(180deg,#9cc6e6 0%,#b9cfd8 30%,#8c7a66 55%,#5f7f4a 80%,#3d5c3a 100%);clip-path:polygon(28% 0,100% 0,100% 100%,0 100%,32% 45%,18% 20%)}
.hero-wedge{position:absolute;right:200px;top:0;width:90px;height:95px;background:#8a8f96;opacity:.75;clip-path:polygon(100% 0,100% 100%,20% 50%)}
.brand{position:relative;display:flex;align-items:center;gap:6px;margin-left:30px;margin-bottom:18px}
.brand-dot{width:10px;height:10px;border-radius:50%;background:var(--sky)}
.brand-name{font-size:13px;font-weight:500;letter-spacing:1.2px;text-transform:uppercase;color:var(--white)}
.hero-title{position:relative;font-size:10.5px;font-weight:700;line-height:1.22;margin-bottom:6px;width:230px}
.hero-title .t1{color:var(--sky)} .hero-title .t2{color:var(--amber)} .hero-title .t3{color:var(--lime)}
.hero p{position:relative;width:285px;font-size:6.2px;margin-bottom:5px}
/* middle */
.mid{height:218px;flex:none;display:flex;gap:14px;padding:10px 26px 8px}
.mid-left{width:210px;display:flex;flex-direction:column}
.stat-box{background:var(--orange);color:var(--white);font-style:italic;font-weight:600;padding:7px 10px;font-size:6px}
.green-box{background:var(--green);color:var(--white);padding:7px 10px;flex:1;border-radius:0 0 4px 4px;display:flex;flex-direction:column;gap:5px}
.green-box .cols{display:flex;gap:14px}
.mid-right{flex:1;display:flex;flex-direction:column;gap:6px;padding-top:4px}
.mid-right .lead{font-weight:700;color:var(--navy)}
.mid-right h4{font-size:6.4px;font-weight:700;color:var(--navy)}
/* blue services */
.services{flex:1;background:var(--blue);color:var(--white);padding:12px 26px}
.services .intro{font-weight:600;font-size:6.8px;margin-bottom:7px}
.services h3,.panel h3{font-size:8px;font-weight:700;margin-bottom:2px}
.two-col{display:flex;gap:18px}
.two-col>div{flex:1}
.services .list{gap:7px;margin-top:6px}
.url{font-weight:700;word-break:break-all}
/* footer */
.footer{height:50px;flex:none;background:var(--navy);color:var(--white);display:flex;align-items:center;gap:26px;padding:0 28px;font-size:9px;font-weight:500}
.footer .item{display:flex;align-items:center;gap:6px}
.footer svg{width:13px;height:13px}
/* right page */
.panel{height:360px;flex:none;background:var(--blue);color:var(--white);padding:14px 26px;display:flex;flex-direction:column;gap:9px}
.panel p{margin-bottom:4px}
.panel .list{gap:3px}
.sub{margin-left:10px}
.review{flex:1;padding:14px 26px 8px;display:flex;flex-direction:column;gap:6px}
.review-top{display:flex;gap:16px;align-items:flex-start}
.review-top>div:first-child{flex:1}
.review h4{font-size:7.5px;font-weight:700;color:var(--navy);margin-bottom:2px}
.quote{width:185px;background:var(--orange);color:var(--white);font-size:7px;font-weight:500;padding:9px 12px;border-radius:3px;position:relative;margin-top:4px}
.quote .by{text-align:right;margin-top:2px}
.quote-mark{position:absolute;font-size:18px;font-weight:700;color:var(--green);line-height:1}
.quote-mark.open{left:-6px;top:-8px}
.quote-mark.close{right:-6px;bottom:-10px}
.deliver{font-weight:700;color:var(--navy)}
.review .list{gap:4px}
</style>
</head>
<body>
<svg width="0" height="0" style="position:absolute">
  <symbol id="tick-white" viewBox="0 0 10 10"><circle cx="5" cy="5" r="5" fill="#ffffff"/><path d="M2.7 5.2 4.4 6.8 7.4 3.5" fill="none" stroke="#2f86cf" stroke-width="1.5"/></symbol>
  <symbol id="tick-green" viewBox="0 0 10 10"><circle cx="5" cy="5" r="5" fill="#ffffff"/><path d="M2.7 5.2 4.4 6.8 7.4 3.5" fill="none" stroke="#69a844" stroke-width="1.5"/></symbol>
  <symbol id="tick-blue" viewBox="0 0 10 10"><circle cx="5" cy="5" r="5" fill="#2f86cf"/><path d="M2.7 5.2 4.4 6.8 7.4 3.5" fill="none" stroke="#ffffff" stroke-width="1.5"/></symbol>
  <symbol id="tick-leaf" viewBox="0 0 10 10"><circle cx="5" cy="5" r="5" fill="#69a844"/><path d="M2.7 5.2 4.4 6.8 7.4 3.5" fill="none" stroke="#ffffff" stroke-width="1.5"/></symbol>
  <symbol id="icon-pin" viewBox="0 0 20 20"><circle cx="10" cy="10" r="10" fill="#f15a24"/><path d="M10 4.5a3.5 3.5 0 0 0-3.5 3.5c0 2.6 3.5 6.5 3.5 6.5s3.5-3.9 3.5-6.5A3.5 3.5 0 0 0 10 4.5z" fill="#fff"/><circle cx="10" cy="8" r="1.3" fill="#f15a24"/></symbol>
  <symbol id="icon-mail" viewBox="0 0 20 20"><circle cx="10" cy="10" r="10" fill="#f15a24"/><rect x="5" y="6.5" width="10" height="7" fill="#fff"/><path d="M5 6.5 10 10.5 15 6.5" fill="none" stroke="#f15a24" stroke-width="1"/></symbol>
  <symbol id="icon-web" viewBox="0 0 20 20"><circle cx="10" cy="10" r="10" fill="#f15a24"/><circle cx="10" cy="10" r="5" fill="none" stroke="#fff" stroke-width="1.1"/><ellipse cx="10" cy="10" rx="2.2" ry="5" fill="none" stroke="#fff" stroke-width="1"/><path d="M5 10h10" stroke="#fff" stroke-width="1"/></symbol>
</svg>

<!-- front -->
<section class="page page-front">
  <header class="hero">
    <div class="hero-wedge"></div>
    <div class="hero-photo" role="img" aria-label="Aerial photo of a downtown city skyline with a bridge and river"></div>
    <div class="brand"><span class="brand-dot"></span><span class="brand-name">Quillmarsh Partners</span></div>
    <h1 class="hero-title"><span class="t1">HarborLeap provides executives and</span> <span class="t2">business owners with clear guidance to</span> <span class="t3">unlock non-financial value ahead of an exit.</span></h1>
    <p>A strong communication and marketing strategy can significantly increase the value of your business leading up to an exit. Buyers are looking to mitigate risk and unlock potential value as a catalyst for clear growth potential.</p>
    <p>Highlighting your company’s success in the marketplace, identifying, and mitigating reputation risks before buyers do, enhancing employee engagement, finding hidden opportunities to boost marketing KPIs and showcasing IP, data, and innovation, can make a significant difference in valuation.</p>
  </header>

  <section class="mid">
    <div class="mid-left">
      <blockquote class="stat-box">US institutional investors believe that Investor Relations (IR) accounts for a total variance of 30% in a company’s valuation – from a premium of 10% for “superb” IR to a discount of 20% for “poor” IR. ---Corvane Research Group, “Harnessing IR’s Power to Impact a Company’s Valuation.”</blockquote>
      <div class="green-box">
        <p>We design and implement communication and marketing strategies that deliver significant increases in brand awareness, identify reputational risks, and enhance brand perception, helping owners and investors to realize premium values for their companies. We support owners and companies through:</p>
        <div class="cols">
          <ul class="list tight">
            <li><svg class="tick"><use href="#tick-green"/></svg>Company Exit Preparation</li>
            <li><svg class="tick"><use href="#tick-green"/></svg>M&amp;A</li>
            <li><svg class="tick"><use href="#tick-green"/></svg>IPO</li>
          </ul>
          <ul class="list tight">
            <li><svg class="tick"><use href="#tick-green"/></svg>Spinoff/Divestiture</li>
            <li><svg class="tick"><use href="#tick-green"/></svg>New Leadership/Investor</li>
          </ul>
        </div>
        <p>Few sellers would list their home without first inspecting, repairing broken items, and making updates to highlight the positive aspects --increasing appeal to buyers. However, countless business owners leave money on the table during corporate exits due to a lack of preparation.</p>
      </div>
    </div>
    <div class="mid-right">
      <p>Our team of executive-level communications and marketing experts brings deep buy and sell-side experience. We have played critical roles in the acquisition, integration and disposition process. Our mix of financial services expertise combined with decades of experience leading internal and external communications, marketing and investor relations teams gives us a unique perspective on identifying and unlocking non-financial areas of value and mitigating non-financial risks before exit.</p>
      <p class="lead">While accounting and investment banking teams are hard at work increasing value from a financial perspective, we help organizations enhance their valuation by identifying areas that will appeal most to buyers and ensuring those elements of your business are visible and memorable to those who matter most.</p>
      <h4>We help companies increase valuation by:</h4>
      <ul class="list tight">
        <li><svg class="tick"><use href="#tick-blue"/></svg>Highlighting value in a clear and visible way</li>
        <li><svg class="tick"><use href="#tick-blue"/></svg>Streamlining the exit process</li>
        <li><svg class="tick"><use href="#tick-blue"/></svg>Identifying potential risks and suggesting mitigation measures</li>
        <li><svg class="tick"><use href="#tick-blue"/></svg>Creating a polished presence in the market ahead of buyer interest</li>
      </ul>
    </div>
  </section>

  <section class="services">
    <p class="intro">HarborLeap provides executives and business owners with clear guidance to unlock value ahead of an exit. Our non-disruptive, ala-carte process enables us to work with sellers on specific areas or to do a complete analysis and recommendation and can include:</p>
    <h3>Brand Analysis and Recommendations</h3>
    <p>Strong brands command a higher valuation. We conduct a brand analysis, providing clear and detailed recommendations to enhance your value proposition and help you stand out from the crowd:</p>
    <div class="two-col">
      <div>
        <ul class="list">
          <li><svg class="tick"><use href="#tick-white"/></svg><span><b>Current external position among competitors--</b> We look at how your brand measures up based on external competitive analysis, positioning in the media and analyst community, and across other digital channels.</span></li>
          <li><svg class="tick"><use href="#tick-white"/></svg><span><b>Physical brand image--</b> A little bit of paint and updated fixtures can go a long way when increasing the value of a home. The same is true for businesses. Our audit evaluates non-disruptive steps your company can take to enhance your brand look and feel before sale.</span></li>
          <li><svg class="tick"><use href="#tick-white"/></svg><span><b>Employee brand perception--</b> We conduct a high-level external audit with recommendations to enhance engagement for current and prospective employees.</span></li>
        </ul>
      </div>
      <div>
        <ul class="list">
          <li><svg class="tick"><use href="#tick-white"/></svg><span><b>Customer brand perception--</b> We conduct a high-level external audit showcasing how customers perceive your brand in the market. We then provide recommendations for enhancing engagement and maximizing value.</span></li>
          <li><svg class="tick"><use href="#tick-white"/></svg><span>A 5% increase in customer retention correlates with at least a 25% increase in profit, according to an analysis by Halbrook &amp; Company. <span class="url">(https://media.halbrook.example/Images/HB_Prescription_cutting_costs.pdf)</span></span></li>
          <li><svg class="tick"><use href="#tick-white"/></svg><span>It costs 5 times more to acquire a new customer than to retain a current one and 16 times more to get new customers to the same spending level as existing ones. <span class="url">(https://growthledger.example/customer-retention-guide-statistics/)</span></span></li>
        </ul>
      </div>
    </div>
  </section>

  <footer class="footer">
    <span class="item"><svg><use href="#icon-pin"/></svg>Austin</span>
    <span class="item"><svg><use href="#icon-mail"/></svg>info@quillmarsh.partners</span>
    <span class="item"><svg><use href="#icon-web"/></svg>https://quillmarsh.partners</span>
  </footer>
</section>

<!-- back -->
<section class="page page-back">
  <section class="panel">
    <div>
      <h3>Digital and Traditional Marketing Analysis and Recommendations</h3>
      <p>How much money are you leaving on the table? Our marketing audits help organizations identify areas of hidden value that can have significant impacts on revenue and valuation. We optimize current activities and uncover new strategies to increase the effectiveness of current marketing spend. Areas we evaluate include:</p>
      <div class="two-col">
        <ul class="list">
          <li><svg class="tick"><use href="#tick-white"/></svg>Website traffic and conversion</li>
          <li><svg class="tick"><use href="#tick-white"/></svg>CRM process review to identify strategies and recommendations to increase conversion and reactive old-leads</li>
          <li><svg class="tick"><use href="#tick-white"/></svg>Email marketing strategy</li>
        </ul>
        <ul class="list">
          <li><svg class="tick"><use href="#tick-white"/></svg>Automations and drip marketing</li>
          <li><svg class="tick"><use href="#tick-white"/></svg>Social media strategy /presence</li>
          <li><svg class="tick"><use href="#tick-white"/></svg>Partnership marketing</li>
          <li><svg class="tick"><use href="#tick-white"/></svg>Paid media analysis/strategy suggestion</li>
        </ul>
      </div>
    </div>
    <div>
      <h3>Messaging and Content Strategy Review and Analysis</h3>
      <p>It’s about your valuation. Full and fair valuation requires a clear, compelling investment case articulated consistently to the right audience at the right time. Messaging to maximize your value in an acquisition or an IPO is quite different from typical selling messages for prospects, customers, or ‘features &amp; business benefits’ for press and analysts. We understand the issues and speak the right language to maximize perception of value with key decision makers.</p>
      <div class="two-col">
        <ul class="list">
          <li><svg class="tick"><use href="#tick-white"/></svg>Review and recommendations of key messaging and value proposition</li>
          <li><svg class="tick"><use href="#tick-white"/></svg>Analysis and recommendation to position key executives likely to remain with the company as thought leaders to help build value</li>
        </ul>
        <ul class="list">
          <li><svg class="tick"><use href="#tick-white"/></svg>Analysis and recommendations to highlight data, IP, and innovation</li>
          <li><svg class="tick"><use href="#tick-white"/></svg>Analysis and recommendations to build employee engagement and retention enhancing your most valuable asset-your team</li>
        </ul>
      </div>
    </div>
    <div>
      <h3>Media and Analyst Strategy Development</h3>
      <p>Positive articles and inclusion in analyst reports pack a powerful punch when preparing your business for sale. We work with clients to develop a media strategy that goes beyond brand awareness, leveraging media to build a digital history of third-party validation targeted to enhance appeal to prospective buyers while generating traffic and connections, to enhance overall value.</p>
      <div class="two-col">
        <ul class="list">
          <li><svg class="tick"><use href="#tick-white"/></svg>Positioning to media and analyst community creating third party market validation</li>
          <li><svg class="tick"><use href="#tick-white"/></svg>Key angle recommendations</li>
        </ul>
        <ul class="list">
          <li><svg class="tick"><use href="#tick-white"/></svg>Announcement timeline &amp; strategy planning to maximize media value of news</li>
          <li class="sub"><svg class="tick"><use href="#tick-white"/></svg>What is newsworthy</li>
          <li class="sub"><svg class="tick"><use href="#tick-white"/></svg>How to position that news for the most significant impact</li>
        </ul>
      </div>
    </div>
  </section>

  <section class="review">
    <div class="review-top">
      <div>
        <h4>“White Hat/Black Hat Review”</h4>
        <p>We take a buyer’s communications and marketing approach to analyzing the client company and provide a “punch list” of things a potential buyer is likely to ask/request in due diligence from a comms/culture/marketing/reputation standpoint to ensure that when potential buyers start screening for sellers and evaluating them, the client company has the upper hand.</p>
      </div>
      <blockquote class="quote">
        <span class="quote-mark open">“</span>
        Strategy without tactics is the slowest route to victory. Tactics without strategy is the noise before defeat.
        <div class="by">– Arden Vale</div>
        <span class="quote-mark close">”</span>
      </blockquote>
    </div>
    <p class="deliver">Once the analysis is complete, we deliver actionable intelligence and recommendations to help leaders identify and quickly unlock areas that will boost value and appeal to prospective buyers. Work products include:</p>
    <ul class="list">
      <li><svg class="tick"><use href="#tick-leaf"/></svg><span><b>Gap Assessment --</b> We provide a comprehensive seller report providing analysis and actionable recommendations to increase your valuation while identifying and mitigating non-financial risks.</span></li>
      <li><svg class="tick"><use href="#tick-leaf"/></svg><span><b>Strategic Roadmap --</b> Clients are given an actionable tactical roadmap based on the recommendation provided. Organizations can choose to implement key areas or include this powerful guide as part of their presentation to prospective buyers to highlight latent potential. The roadmap provides actionable steps buyers can take upon close as they make their case for your business with their investment committees.</span></li>
    </ul>
    <p>Once the strategy integration roadmap is complete, your team can implement it on your timeline, we can work with your team providing guidance and executive-level support, or we can fully execute deliverables with our robust capabilities and team.</p>
    <p>Our value proposition, based on delivering outcomes rather than just outputs, means that you receive the benefit and capability of deeply experienced corporate communications leaders without adding headcount or the time to identify, recruit, onboard and retain a new team member.</p>
    <p>We help organizations enhance their valuation by identifying areas that will appeal most to buyers and ensuring those elements of your business are visible and memorable to those who matter most.</p>
    <p>HarborLeap helps sellers maximize valuation and unlock hidden potential ahead of an exit--ensuring money is not left on the table.</p>
  </section>

  <footer class="footer">
    <span class="item"><svg><use href="#icon-pin"/></svg>Austin</span>
    <span class="item"><svg><use href="#icon-mail"/></svg>info@quillmarsh.partners</span>
    <span class="item"><svg><use href="#icon-web"/></svg>https://quillmarsh.partners</span>
  </footer>
</section>
</body>
</html>
```